Milos Meadow Plant Hire WEB

Milos Meadow are a small family owned business specialising in hire of indoor horticultural plants. They have been operating for more than 20 years in the local New Zealand market providing long and short term plant hire for businesses and events.

They offer a wide range of mostly tropical and indigenous plants for hire and Milos Meadow staff maintain all hire plants on a regular basis.

MORE PHOTOS AVAILABLE ON REQUEST if required

Please note - this should be a small 3 pager - home/about - products - gallery
Contact Us can be a button or on home page. Note - this is a small owner operated business.

Target Market(s)

Commercial, offices, entrance foyers, receptions, restaurants, promotions, trade shows, events, corporate and private functions

Industry/Entity Type

Business

Requirements
Must have
• Must remain integral to existing branding and include the current company logo. Should maintain existing corporate colours. Requires an enquiry page for people to contact the company via email (this can be a mailto page), also requires a page explaining about the company, and one detailing the types of hire available together with types of plans for hire. The site also needs a gallery that can be added to over time to show the various plants and their applications.
Nice to have
• It would be nice to have a facility on the gallery where a couple of detail lines could be added to explain the plant types, location etc

PREFER A WORDPRESS SOLUTION - BUT OPEN TO SUGGESTIONS
Should not have
• The site should not be overly complex. It should be simple for the client to self manage (add/ remove photos, edit text) It should be quick to load and simple to navigate.

```html
<!DOCTYPE html>
<html lang="en">
<head>
<meta charset="utf-8">
<title>Milos Meadow Plant Hire – About Us</title>
<link href="https://fonts.googleapis.com/css2?family=Questrial&family=Montserrat:wght@700;800&display=swap" rel="stylesheet">
<style>
  :root {
    --green-dark: #3b6a0b;
    --green-band: #3f6f0c;
    --green-lime: #9aae12;
    --green-nav: #6e9c12;
    --text-green: #3d6a10;
    --ink: #1c1c1c;
    --white: #ffffff;
    --shadow: rgba(0,0,0,0.18);
  }
  * { margin: 0; padding: 0; box-sizing: border-box; }
  html, body { width: 1200px; height: 800px; overflow: hidden; background: var(--white); }
  .page { position: relative; width: 1200px; height: 800px; overflow: hidden; font-family: "Questrial", sans-serif; }
  .backdrop { position: absolute; inset: 0; }

  .social { position: absolute; top: 7px; right: 18px; display: flex; gap: 10px; list-style: none; }
  .social li { width: 20px; height: 20px; border-radius: 50%; background: var(--white); }

  .brand { position: absolute; left: 38px; top: 112px; width: 140px; text-align: center;
    font-family: "Questrial", sans-serif; font-size: 19px; color: var(--ink); }

  .nav-rule { position: absolute; left: 186px; top: 53px; width: 2px; height: 152px; background: var(--green-dark); }
  .main-nav { position: absolute; left: 203px; top: 93px; list-style: none; }
  .main-nav li { font-size: 19px; line-height: 18.5px; color: var(--ink); text-transform: uppercase; }
  .main-nav li.is-current { color: var(--green-nav); }

  .page-title { position: absolute; left: 366px; top: 196px; font-family: "Montserrat", sans-serif;
    font-weight: 800; line-height: 0.8; text-align: right; width: 292px; }
  .page-title .word-about { display: block; font-size: 88px; color: var(--green-dark); letter-spacing: -2px; }
  .page-title .word-us { display: block; font-size: 88px; color: var(--green-lime); letter-spacing: -2px; margin-top: 2px; }

  .about-rule { position: absolute; left: 687px; top: 100px; width: 2px; height: 306px; background: var(--green-dark); }
  .about-copy { position: absolute; left: 706px; top: 98px; width: 420px; color: var(--text-green);
    font-size: 17px; line-height: 17.5px; }
  .about-copy p + p { margin-top: 17px; }

  .tagline { position: absolute; left: 0; top: 676px; width: 1200px; color: var(--white);
    font-family: "Montserrat", sans-serif; font-weight: 700; text-transform: uppercase; }
  .tagline .line { position: absolute; white-space: nowrap; line-height: 1; }
  .tagline .line-one { left: 441px; top: 0; }
  .tagline .line-two { left: 344px; top: 36px; }
  .tagline .small { font-size: 15px; }
  .tagline .big { font-size: 44px; letter-spacing: -1px; }

  .site-footer { position: absolute; left: 0; bottom: 0; width: 1200px; height: 25px; background: var(--green-band);
    color: var(--white); font-family: Arial, sans-serif; font-size: 10px; text-align: right; padding: 8px 34px 0 0; }
</style>
</head>
<body>
<div class="page">
  <svg class="backdrop" width="1200" height="800" viewBox="0 0 1200 800">
    <defs>
      <linearGradient id="swirlTone" x1="0" y1="0" x2="1" y2="1">
        <stop offset="0" stop-color="#7c7a1e"/>
        <stop offset="0.5" stop-color="#4f6a16"/>
        <stop offset="1" stop-color="#8a9a4a"/>
      </linearGradient>
      <linearGradient id="meadowTone" x1="0" y1="0" x2="1" y2="0">
        <stop offset="0" stop-color="#5d6b2a"/>
        <stop offset="0.45" stop-color="#7d8548"/>
        <stop offset="0.75" stop-color="#c9c4a0"/>
        <stop offset="1" stop-color="#e6e2cf"/>
      </linearGradient>
      <filter id="panelShadow" x="-10%" y="-10%" width="120%" height="130%">
        <feDropShadow dx="0" dy="4" stdDeviation="5" flood-color="#000" flood-opacity="0.25"/>
      </filter>
    </defs>

    <rect class="top-band" x="400" y="0" width="800" height="32" fill="var(--green-band)"/>

    <polygon class="swirl-field" role="img" aria-label="Decorative spiral pattern filled with a meadow photograph"
      points="0,330 300,318 1200,660 1200,666 0,666" fill="url(#swirlTone)" opacity="0.9"/>

    <polygon class="diagonal-panel" points="290,300 1200,250 1200,640 260,400" fill="var(--white)" filter="url(#panelShadow)"/>
    <polygon class="left-panel" points="0,210 265,325 300,330 0,360" fill="var(--white)" filter="url(#panelShadow)"/>
    <polygon class="top-panel" points="0,0 415,0 265,325 0,205" fill="var(--white)" filter="url(#panelShadow)"/>

    <rect class="meadow-photo" role="img" aria-label="Photograph of a daisy meadow" x="0" y="666" width="1200" height="110" fill="url(#meadowTone)"/>
  </svg>

  <ul class="social" aria-label="Social links">
    <li></li><li></li><li></li>
  </ul>

  <div class="brand">Milos Meadow</div>
  <div class="nav-rule"></div>
  <ul class="main-nav">
    <li class="is-current">About Us</li>
    <li>Services</li>
    <li>Gallery</li>
    <li>Contact Us</li>
  </ul>

  <h1 class="page-title"><span class="word-about">ABOUT</span><span class="word-us">US</span></h1>

  <div class="about-rule"></div>
  <div class="about-copy">
    <p>Milos Meadow is a family owned, Kowhai Bay based business established over 25 years ago</p>
    <p>We can enhance your workplace by introducing quality indoor plants in attractive planters Creating a natural green environment with Milos Meadow plants will help improve indoor air quality, increase staff wellness and productivity</p>
    <p>Our range of tropical and native plants will enhance your conference or event by creating a more relaxing atmosphere for your delegates or clients. Milos Meadow staff can advise on plant arrangement, deliver and setup for each event</p>
    <p>We are committed to providing prompt friendly service to all our customers ensuring that your workplace or function is enhanced with quality</p>
  </div>

  <div class="tagline">
    <div class="line line-one"><span class="small">Quality</span><span class="big">Indoor</span></div>
    <div class="line line-two"><span class="small">and </span><span class="big">Outdoor</span><span class="small">plants</span></div>
  </div>

  <footer class="site-footer">Copyright © 2013 All rights reserved. | Privacy Practices</footer>
</div>
</body>
</html>
```